Letterhead design for business

Looking for an attractive and professional letterhead that uses the logo that is attached below.

Target Market(s)

Potential bankruptcy clients.

Industry/Entity Type

Legal

Colors

Designer to choose colors to be used in the design.

Requirements
Must have
• Address for locations, phone number, and website address.
• Addresses are on website ferncoveadvice.example. Use following phone number (for tracking purposes): 555-013-8274

```html
<!DOCTYPE html>
<html lang="en">
<head>
<meta charset="utf-8">
<title>Ferncove Law Group Letterhead</title>
<link rel="stylesheet" href="https://fonts.googleapis.com/css2?family=Source+Sans+3:wght@400;600&family=Open+Sans:wght@400;600&display=swap">
<style>
  :root {
    --paper: #ffffff;
    --ink: #565656;
    --ink-dark: #333333;
    --rule: #4a4a4a;
    --accent: #7dbf8a;
    --signature-tone: #e4e4e4;
  }
  html, body {
    margin: 0;
    padding: 0;
    width: 986px;
    height: 1200px;
    overflow: hidden;
    background: var(--paper);
  }
  .letterhead {
    position: relative;
    width: 986px;
    height: 1200px;
    background: var(--paper);
    font-family: "Source Sans 3", "Myriad Pro", sans-serif;
    color: var(--ink);
  }
  .brand {
    position: absolute;
    top: 170px;
    left: 0;
    width: 986px;
    display: flex;
    justify-content: center;
    align-items: center;
    gap: 14px;
  }
  .brand-dot {
    width: 22px;
    height: 22px;
    border-radius: 50%;
    background: var(--accent);
  }
  .brand-name {
    font-size: 38px;
    font-weight: 600;
    color: var(--ink-dark);
    letter-spacing: 0.5px;
  }
  .rule {
    position: absolute;
    height: 2px;
    background: var(--rule);
  }
  .rule-top { top: 230px; left: 85px; width: 803px; }
  .rule-bottom { top: 1068px; left: 90px; width: 804px; }
  .body-copy {
    position: absolute;
    top: 258px;
    left: 102px;
    width: 796px;
    font-size: 16.4px;
    line-height: 21px;
    text-align: justify;
  }
  .body-copy p { margin: 0 0 21px; }
  .signature {
    position: absolute;
    top: 962px;
    left: 694px;
    width: 165px;
    height: 34px;
    background: var(--signature-tone);
  }
  .signer {
    position: absolute;
    top: 1005px;
    left: 700px;
    width: 170px;
    text-align: center;
    font-size: 16.5px;
  }
  .address {
    position: absolute;
    top: 1079px;
    left: 0;
    width: 986px;
    text-align: center;
    font-family: "Open Sans", sans-serif;
    font-size: 11.5px;
    font-weight: 600;
    letter-spacing: 1.3px;
    color: var(--ink-dark);
  }
  .contacts {
    position: absolute;
    top: 1114px;
    left: 0;
    width: 986px;
    display: flex;
    justify-content: center;
    gap: 30px;
    font-family: "Open Sans", sans-serif;
    font-size: 11.5px;
    font-weight: 600;
    letter-spacing: 0.8px;
    color: var(--ink-dark);
  }
  .contact { display: flex; align-items: center; gap: 8px; }
  .contact svg { width: 11px; height: 11px; fill: var(--accent); }
</style>
</head>
<body>
<main class="letterhead">
  <header class="brand">
    <span class="brand-dot"></span>
    <span class="brand-name">Ferncove Law Group</span>
  </header>

  <div class="rule rule-top"></div>

  <section class="body-copy">
    <p>Lorem ipsum dolor sit amet, consectetur adipiscing elit, sed do eiusmod tempor incididunt ut labore et dolore magna aliqua. Ut enim ad minim veniam, quis nostrud exercitation ullamco laboris nisi ut aliquip ex ea commodo consequat. Duis aute irure dolor in reprehenderit in voluptate velit esse cillum dolore eu fugiat nulla pariatur. Excepteur sint occaecat cupidatat non proident, sunt in culpa qui officia deserunt mollit anim id est laborum</p>
    <p>Sed ut perspiciatis unde omnis iste natus error sit voluptatem accusantium doloremque laudantium, totam rem aperiam, eaque ipsa quae ab illo inventore veritatis et quasi architecto beatae vitae dicta sunt explicabo. Nemo enim ipsam voluptatem quia voluptas sit aspernatur aut odit aut fugit, sed quia consequuntur magni dolores eos qui ratione voluptatem sequi nesciunt. Neque porro quisquam est, qui dolorem ipsum quia dolor sit amet, consectetur, adipisci velit, sed quia non numquam eius modi tempora incidunt ut labore et dolore magnam aliquam quaerat voluptatem. Ut enim ad minima veniam, quis nostrum exercitationem ullam corporis suscipit laboriosam, nisi ut aliquid ex ea commodi consequatur? Quis autem vel eum iure reprehenderit qui in ea voluptate velit esse quam nihil molestiae consequatur, vel illum qui dolorem eum fugiat quo voluptas nulla pariatur?</p>
    <p>Lorem ipsum dolor sit amet, consectetur adipiscing elit, sed do eiusmod tempor incididunt ut labore et dolore magna aliqua. Ut enim ad minim veniam, quis nostrud exercitation ullamco laboris nisi ut aliquip ex ea commodo consequat. Duis aute irure dolor in reprehenderit in voluptate velit esse cillum dolore eu fugiat nulla pariatur. Excepteur sint occaecat cupidatat non proident, sunt in culpa qui officia deserunt mollit anim id est laborum</p>
    <p>Sed ut perspiciatis unde omnis iste natus error sit voluptatem accusantium doloremque laudantium, totam rem aperiam, eaque ipsa quae ab illo inventore veritatis et quasi architecto beatae vitae dicta sunt explicabo. Nemo enim ipsam voluptatem quia voluptas sit aspernatur aut odit aut fugit, sed quia consequuntur magni dolores eos qui ratione voluptatem sequi nesciunt. Neque porro quisquam est, qui dolorem ipsum quia dolor sit amet, consectetur, adipisci velit, sed quia non numquam eius modi tempora incidunt ut labore et dolore magnam aliquam quaerat voluptatem. Ut enim ad minima veniam, quis nostrum exercitationem ullam corporis suscipit laboriosam, nisi ut aliquid ex ea commodi consequatur? Quis autem vel eum iure reprehenderit qui in ea voluptate velit esse quam nihil molestiae consequatur, vel illum qui dolorem eum fugiat quo voluptas nulla pariatur?</p>
  </section>

  <div class="signature" role="img" aria-label="Handwritten signature"></div>
  <div class="signer">Name Name</div>

  <div class="rule rule-bottom"></div>

  <footer>
    <div class="address">418 Harborview Ave., Suite #1400 Millbrook, Georgia 30999</div>
    <div class="contacts">
      <span class="contact">
        <svg viewBox="0 0 24 24" aria-hidden="true"><path d="M6.6 10.8a15.1 15.1 0 0 0 6.6 6.6l2.2-2.2a1 1 0 0 1 1-.25 11.4 11.4 0 0 0 3.6.57 1 1 0 0 1 1 1V20a1 1 0 0 1-1 1A17 17 0 0 1 3 4a1 1 0 0 1 1-1h3.5a1 1 0 0 1 1 1c0 1.25.2 2.45.57 3.6a1 1 0 0 1-.25 1z"/></svg>
        555-013-8274
      </span>
      <span class="contact">
        <svg viewBox="0 0 24 24" aria-hidden="true"><path d="M2 5h20v14H2z M2 5l10 7 10-7" /></svg>
        info@ferncoveadvice.example
      </span>
      <span class="contact">
        <svg viewBox="0 0 24 24" aria-hidden="true"><circle cx="12" cy="12" r="10"/></svg>
        www.ferncoveadvice.example
      </span>
    </div>
  </footer>
</main>
</body>
</html>
```